Door Hanger General Contractor

design high quality marketing piece to promote our general contractor business.
Use all content create badges, banners, bubbles, boxes ect to highlight text.
Template format is uploaded in images
Make font as large as possible, minimize negative space, fill areas
FRONT SIDE
Your Neighbor Just Remodeled
Come See Our Work at:
(under this create blank white box placeholder for address)
LOVE YOUR HOME AGAIN!
WE MAKE REMODELING EASY
FREE 3D DESIGN SERVICES
FREE ESTIMATES
LICENSED GENERAL CONTRACTORS
We Specialize in:
Kitchen Remodel
Bathroom Remodel
Interior/Exterior Painting
Flooring: Carpet, Vinyl, Wood & Tile
Energy Efficient Upgrades
Window/Door Replacement
WATER & MOLD DAMAGE
BACK SIDE
GET STARTED IN 3 SIMPLE STEPS:
1 ORDER FREE ESTIMATE & DESIGN
2 APPROVE ESTIMATE & DESIGN
3 HEARTHWAY RENOVATORS BUILDS YOUR DREAM
Thinking About Selling?
We Buy Homes
GET CASH OFFER
SELLING MADE EASY
CALL NOW!!
Hearthway Renovators Inc.
858-555-0174 Call/Text
BrightGableHomes.example
CSLB# 4087261
home owners
General Contractor

```html
<!DOCTYPE html>
<html lang="en">
<head>
<meta charset="utf-8">
<title>Hearthway Renovators – Door Hanger</title>
<link rel="stylesheet" href="https://fonts.googleapis.com/css2?family=Oswald:wght@500;600;700&family=Poppins:wght@400;500;600;700;800&display=swap">
<style>
  :root{
    --stage:#c3cbd8;
    --ink:#111111;
    --night:#151515;
    --blue:#3b7bec;
    --blue-light:#6fa0f5;
    --blue-deep:#1f5fe0;
    --red:#e11414;
    --yellow:#ffe600;
    --white:#ffffff;
    --grey-text:#222;
  }
  *{box-sizing:border-box;margin:0;padding:0}
  html,body{width:1200px;height:1200px;overflow:hidden}
  body{background:var(--stage);font-family:"Poppins",sans-serif;position:relative;color:var(--ink)}
  .hanger{position:absolute;background:var(--white);overflow:hidden;box-shadow:0 10px 24px rgba(40,50,70,.25)}
  .hanger--front{left:178px;top:170px;width:360px;height:900px}
  .hanger--back{left:670px;top:159px;width:366px;height:912px}
  .hanger__hole{position:absolute;top:43px;width:223px;height:178px;background:var(--stage);border-radius:84px 84px 0 0;z-index:3}
  .hanger--front .hanger__hole{left:70px}
  .hanger--back .hanger__hole{left:71px}
  .hanger__dark{position:absolute;left:0;top:0;width:100%;background:var(--night)}
  .hanger__photo{position:absolute;left:0;width:100%;background:linear-gradient(180deg,#151515 0%,#2b2c2e 45%,#3a3b3d 80%,#2a2a2b 100%)}
  .abs{position:absolute;white-space:nowrap}
  .center{left:0;width:100%;text-align:center}

  /* front */
  .brand{top:290px;display:flex;justify-content:center;align-items:center;gap:8px;color:var(--white);font-weight:500;font-size:13px;letter-spacing:1.5px}
  .brand__dot{width:12px;height:12px;border-radius:50%;border:1.5px solid var(--white)}
  .headline-1{top:328px;font-weight:500;font-size:30px;color:var(--white);letter-spacing:-.5px;line-height:1}
  .headline-2{top:358px;font-weight:800;font-size:29px;color:var(--blue);letter-spacing:-.5px;line-height:1}
  .see-work{top:391px;font-size:11.5px;letter-spacing:4.5px;color:var(--white);font-weight:500}
  .address-box{left:39px;top:413px;width:284px;height:30px;background:var(--white);border:2px solid var(--blue);border-radius:6px}
  .love{left:31px;top:457px;font-weight:800;font-size:21px;line-height:.98;color:var(--white)}
  .home-again{left:106px;top:455px;font-family:"Oswald",sans-serif;font-weight:500;font-size:45px;line-height:1;color:var(--blue);letter-spacing:-1.2px}
  .easy{top:506px;font-size:15.5px;letter-spacing:3.4px;color:var(--white);font-weight:500}
  .tile{position:absolute;top:536px;height:70px;transform:skewX(-12deg);overflow:hidden}
  .tile--design{left:44px;width:86px;background:linear-gradient(135deg,#d9b48a,#f1e7dc 55%,#b9935f)}
  .tile--license{left:142px;width:92px;background:linear-gradient(135deg,#8cb6e6,#e7eef7 55%,#6c7a8c)}
  .tile-label{position:absolute;top:606px;height:26px;transform:skewX(-12deg);display:flex;align-items:center;justify-content:center;text-align:center}
  .tile-label span{transform:skewX(12deg);font-size:8.2px;font-weight:700;line-height:1.1;color:var(--white);white-space:nowrap}
  .tile-label--design{left:38px;width:94px;background:#1d1d1d}
  .tile-label--license{left:136px;width:98px;background:var(--blue)}
  .burst{left:227px;top:522px;width:104px;height:122px}
  .burst__text{left:230px;top:572px;width:98px;text-align:center;font-family:"Oswald",sans-serif;font-weight:600;font-size:17px;line-height:1.05;color:var(--yellow)}
  .special{left:24px;top:647px;width:311px;height:118px;border:1.5px solid var(--blue)}
  .special__tab{position:absolute;left:-1px;top:-1px;width:148px;height:22px;background:var(--blue);clip-path:polygon(0 0,100% 0,88% 100%,0 100%);color:var(--white);font-size:13px;font-weight:600;padding-left:12px;line-height:22px;white-space:nowrap}
  .special__list{position:absolute;list-style:none;font-size:10.6px;font-weight:500;line-height:1.25;color:var(--grey-text);white-space:nowrap}
  .special__list li{position:relative;padding-left:20px;margin-bottom:9px}
  .special__list li::before{content:"";position:absolute;left:0;top:2px;width:11px;height:11px;border-radius:50%;background:var(--blue)}
  .special__list li::after{content:"";position:absolute;left:3.5px;top:4.5px;width:3px;height:5px;border:solid var(--white);border-width:0 1.5px 1.5px 0;transform:rotate(45deg)}
  .special__list--a{left:12px;top:30px}
  .special__list--b{left:172px;top:8px}
  .special__list--b li{margin-bottom:6px}
  .damage{left:36px;top:754px;width:288px;height:24px;background:var(--red);border-radius:3px;color:var(--yellow);font-weight:800;font-size:18px;letter-spacing:.6px;text-align:center;line-height:24px}
  .call-now{left:23px;top:789px;font-weight:800;font-size:24px;line-height:.95;color:var(--red)}
  .company{left:121px;top:792px;font-size:10px;font-weight:600;letter-spacing:1.9px;color:var(--ink)}
  .phone-row{left:121px;top:806px;display:flex;align-items:center;gap:3px}
  .icon-round{width:17px;height:17px;border-radius:50%;background:var(--blue);display:flex;align-items:center;justify-content:center}
  .phone-row__or{font-family:"Oswald",sans-serif;font-weight:600;font-size:14px}
  .phone{font-family:"Oswald",sans-serif;font-weight:600;font-size:30px;line-height:1;color:var(--ink);margin-left:5px;letter-spacing:-.3px}
  .web-bar{left:23px;height:23px;background:var(--ink);border-radius:12px;display:flex;align-items:center;justify-content:space-between;overflow:hidden}
  .web-bar__url{color:var(--white);font-weight:700;font-size:10.5px;padding-left:12px;white-space:nowrap}
  .web-bar__lic{height:100%;background:var(--blue);border-radius:12px;color:var(--white);font-weight:700;font-size:10.5px;display:flex;align-items:center;padding:0 10px;white-space:nowrap;flex-shrink:0}
  .hanger--front .web-bar{top:847px;width:319px}

  /* back */
  .get-started{top:262px;font-size:28px;letter-spacing:4.2px;color:var(--white);font-weight:500}
  .big-three{left:88px;top:292px;font-weight:800;font-size:92px;line-height:1;color:var(--blue)}
  .simple-steps{left:143px;top:300px;font-weight:800;font-size:36px;line-height:1.03;color:var(--white);letter-spacing:-.5px}
  .ribbon{left:0;top:380px;width:366px;height:300px}
  .step-text{position:absolute;color:var(--white);font-weight:700;font-size:14.5px;line-height:1.08;white-space:nowrap}
  .step-text--1{left:114px;top:406px}
  .step-text--2{left:110px;top:510px}
  .step-text--3{left:199px;top:601px}
  .selling{left:30px;top:694px;width:308px;height:32px;background:var(--red);border-radius:4px;color:var(--yellow);font-weight:800;font-size:19.5px;text-align:center;line-height:32px;letter-spacing:.2px}
  .pill{position:absolute;top:740px;height:38px;display:flex;align-items:center}
  .pill__icon{width:38px;height:38px;border-radius:50%;background:var(--blue);border:3px solid #b8cff7;display:flex;align-items:center;justify-content:center;position:relative;z-index:2}
  .pill__label{height:29px;border:1.2px solid var(--ink);border-radius:15px;margin-left:-10px;padding:0 10px 0 16px;display:flex;align-items:center;font-size:9.6px;font-weight:700;line-height:1.05;white-space:nowrap}
  .pill--buy{left:25px}
  .pill--cash{left:124px}
  .pill--easy{left:230px}
  .divider{left:21px;top:790px;width:320px;border-top:1.2px dashed var(--blue)}
  .seal{left:24px;top:809px}
  .cert{left:75px;top:820px;width:64px;height:30px;border:1.5px solid var(--ink);border-radius:3px;background:#1c1c1c}
  .b-call{left:144px;top:800px;color:var(--red);font-weight:800;font-size:11.5px;letter-spacing:1.2px}
  .b-company{left:144px;top:816px;font-size:9px;font-weight:600;letter-spacing:1.5px}
  .b-calltext{left:144px;top:834px;color:var(--blue);font-weight:700;font-size:10px;line-height:.95}
  .b-phone{left:203px;top:826px;font-family:"Oswald",sans-serif;font-weight:600;font-size:28px;line-height:1;letter-spacing:-.3px}
  .hanger--back .web-bar{top:861px;width:322px}
</style>
</head>
<body>

<section class="hanger hanger--front" aria-label="Door hanger front">
  <div class="hanger__dark" style="height:584px"></div>
  <div class="hanger__photo" style="top:222px;height:362px" role="img" aria-label="Dimly lit modern living room interior"></div>
  <div class="hanger__hole"></div>

  <div class="abs center brand"><span class="brand__dot"></span><span>HEARTHWAY RENOVATORS</span></div>
  <h1 class="abs center headline-1">YOUR NEIGHBOR</h1>
  <h2 class="abs center headline-2">JUST REMODELED</h2>
  <p class="abs center see-work">COME SEE OUR WORK AT</p>
  <div class="abs address-box" aria-label="Address placeholder"></div>
  <p class="abs love">LOVE<br>YOUR</p>
  <p class="abs home-again">HOME AGAIN!</p>
  <p class="abs center easy">WE MAKE REMODELING EASY</p>

  <div class="tile tile--design" role="img" aria-label="Bright remodeled kitchen with wood framing"></div>
  <div class="tile tile--license" role="img" aria-label="Contractor holding a clipboard in front of a house"></div>
  <div class="tile-label tile-label--design"><span>FREE 3D DESIGN<br>SERVICES</span></div>
  <div class="tile-label tile-label--license"><span>LICENSED GENERAL<br>CONTRACTOR</span></div>

  <svg class="abs burst" viewBox="0 0 104 122" aria-hidden="true">
    <polygon fill="#e11414" points="52,0 60,12 74,5 76,20 91,19 86,33 100,39 90,50 102,61 90,72 100,83 86,89 91,103 76,102 74,117 60,110 52,122 44,110 30,117 28,102 13,103 18,89 4,83 14,72 2,61 14,50 4,39 18,33 13,19 28,20 30,5 44,12"/>
    <rect x="38" y="22" width="22" height="27" rx="3" fill="#f2f2f2"/>
    <rect x="41" y="25" width="16" height="6" fill="#9fb9e0"/>
    <circle cx="64" cy="44" r="5" fill="#f4b31c"/>
  </svg>
  <p class="abs burst__text">FREE<br>ESTIMATES</p>

  <div class="abs special">
    <div class="special__tab">WE SPECIALIZE IN</div>
    <ul class="special__list special__list--a">
      <li>Kitchen Remodel</li>
      <li>Bathroom Remodel</li>
      <li>Flooring: Carpet,<br>Vinyl, Wood &amp; Tile</li>
    </ul>
    <ul class="special__list special__list--b">
      <li>Window/Door<br>Replacement</li>
      <li>Interior/Exterior<br>Painting</li>
      <li>Energy Efficient<br>Upgrades</li>
    </ul>
  </div>
  <p class="abs damage">WATER &amp; MOLD DAMAGE</p>

  <p class="abs call-now">CALL<br>NOW!!</p>
  <p class="abs company">HEARTHWAY RENOVATORS INC.</p>
  <div class="abs phone-row">
    <span class="icon-round"><svg width="10" height="10" viewBox="0 0 24 24"><path fill="#fff" d="M6.6 10.8a15.1 15.1 0 0 0 6.6 6.6l2.2-2.2c.3-.3.7-.4 1-.2 1.1.4 2.3.6 3.6.6.6 0 1 .4 1 1V20c0 .6-.4 1-1 1A17 17 0 0 1 3 4c0-.6.4-1 1-1h3.5c.6 0 1 .4 1 1 0 1.3.2 2.5.6 3.6.1.3 0 .7-.2 1z"/></svg></span>
    <span class="phone-row__or">OR</span>
    <span class="icon-round"><svg width="10" height="10" viewBox="0 0 24 24"><ellipse cx="12" cy="11" rx="9" ry="7.5" fill="#fff"/><circle cx="8" cy="11" r="1.3" fill="#3b7bec"/><circle cx="12" cy="11" r="1.3" fill="#3b7bec"/><circle cx="16" cy="11" r="1.3" fill="#3b7bec"/></svg></span>
    <span class="phone">858-555-0174</span>
  </div>
  <div class="abs web-bar"><span class="web-bar__url">www.BrightGableHomes.example</span><span class="web-bar__lic">CSLB# 4087261</span></div>
</section>

<section class="hanger hanger--back" aria-label="Door hanger back">
  <div class="hanger__dark" style="height:538px"></div>
  <div class="hanger__photo" style="top:222px;height:316px" role="img" aria-label="Dimly lit modern living room interior"></div>
  <div class="hanger__hole"></div>

  <p class="abs center get-started">GET STARTED IN</p>
  <p class="abs big-three">3</p>
  <p class="abs simple-steps">SIMPLE<br>STEPS</p>

  <svg class="abs ribbon" viewBox="0 0 366 300" aria-hidden="true">
    <polygon points="21,95 64,15 218,15 264,95" fill="#6fa0f5"/>
    <polygon points="21,95 64,15 98,15 98,95" fill="#5b91f2"/>
    <text x="66" y="88" font-family="Poppins,sans-serif" font-weight="800" font-size="92" fill="#4f86ee" opacity=".75">1</text>
    <polygon points="21,95 55,95 67,111 29,111" fill="#3368d6"/>
    <polygon points="29,111 295,111 346,194 74,194" fill="#4a86ef"/>
    <text x="238" y="190" font-family="Poppins,sans-serif" font-weight="800" font-size="96" fill="#2f6ae6" opacity=".9">2</text>
    <polygon points="300,194 346,194 352,208 313,208" fill="#1b4fbf"/>
    <polygon points="107,208 352,208 306,290 150,290" fill="#1f5fe0"/>
    <text x="140" y="285" font-family="Poppins,sans-serif" font-weight="800" font-size="92" fill="#1a54cc">3</text>
    <g transform="translate(259,18)" fill="none" stroke="#111" stroke-width="2.6" stroke-linejoin="round" stroke-linecap="round">
      <path d="M4 30 L33 4 L62 30"/>
      <path d="M12 24 V62 H54 V24"/>
      <path d="M24 32 l10 -6 6 6 -6 6z"/>
      <path d="M37 35 L58 60"/>
    </g>
    <g transform="translate(44,218)" fill="none" stroke="#111" stroke-width="2.6" stroke-linejoin="round" stroke-linecap="round">
      <path d="M4 24 H40 V62 H4z"/>
      <path d="M22 38 c-5 7 -5 12 0 12 c5 0 5-5 0-12z"/>
      <path d="M28 20 L54 0 L66 12 L42 34"/>
      <path d="M54 22 L68 40 L62 46 L48 30"/>
    </g>
  </svg>
  <p class="step-text step-text--1">ORDER FREE<br>ESTIMATE &amp;<br>DESIGN</p>
  <p class="step-text step-text--2">APPROVE<br>ESTIMATE &amp;<br>DESIGN</p>
  <p class="step-text step-text--3">HEARTHWAY<br>RENOVATORS<br>BUILDS YOUR<br>DREAM</p>

  <p class="abs selling">THINKING ABOUT SELLING?</p>

  <div class="pill pill--buy">
    <span class="pill__icon"><svg width="18" height="18" viewBox="0 0 24 24" fill="none" stroke="#fff" stroke-width="2" stroke-linejoin="round"><path d="M3 11 L12 3 L21 11"/><path d="M6 9 V21 H18 V9"/><path d="M10 21 V15 H14 V21"/></svg></span>
    <span class="pill__label">WE BUY<br>HOMES</span>
  </div>
  <div class="pill pill--cash">
    <span class="pill__icon"><svg width="18" height="18" viewBox="0 0 24 24" fill="none" stroke="#fff" stroke-width="2"><circle cx="12" cy="9" r="6"/><path d="M3 20 h6 l3 -2 h6" stroke-linecap="round"/><text x="9.4" y="12" font-size="8" fill="#fff" stroke="none" font-family="Poppins,sans-serif" font-weight="700">$</text></svg></span>
    <span class="pill__label">GET CASH<br>OFFER</span>
  </div>
  <div class="pill pill--easy">
    <span class="pill__icon"><svg width="18" height="18" viewBox="0 0 24 24" fill="none" stroke="#fff" stroke-width="2" stroke-linejoin="round" stroke-linecap="round"><path d="M6 8 L12 3 L18 8 V13 H6z"/><path d="M3 17 l5 -3 h5 l3 3 l-3 3 h-6"/><path d="M21 17 l-4 -3"/></svg></span>
    <span class="pill__label">SELLING<br>MADE EASY</span>
  </div>

  <div class="abs divider"></div>

  <svg class="abs seal" width="44" height="52" viewBox="0 0 44 52" aria-label="Insurance claim badge">
    <path d="M22 2 L40 8 V26 C40 38 32 46 22 50 C12 46 4 38 4 26 V8z" fill="#1c1c1c" stroke="#111" stroke-width="2"/>
    <path d="M22 7 L35 11.5 V26 C35 35 29 41 22 44 C15 41 9 35 9 26 V11.5z" fill="none" stroke="#fff" stroke-width="1.2"/>
    <rect x="0" y="30" width="44" height="8" fill="#e11414"/>
  </svg>
  <div class="abs cert" aria-label="Certification badge"></div>

  <p class="abs b-call">CALL NOW!!</p>
  <p class="abs b-company">HEARTHWAY RENOVATORS INC.</p>
  <p class="abs b-calltext">(CALL<br>OR TEXT)</p>
  <p class="abs b-phone">858-555-0174</p>
  <div class="abs web-bar"><span class="web-bar__url">www.BrightGableHomes.example</span><span class="web-bar__lic">CSLB# 4087261</span></div>
</section>

</body>
</html>
```